New Business Card Design Project

Hi! I would like for you to design a business card for our aesthetic injections business. We offer Zelvia, filler, skin care. I would like it to be elegant, feminine, modern and sleek/clean. I like black/gold foil/ivory/parchment colors. It can be either one or two sided. I would like matte black with gold foil logo on one side and ivory with gold foil information on the other side

Target Market(s)

target market is the discerning woman who wants to look her best

Industry/Entity Type

beauty

Contact Information for Business Card

logo, name, phone, email, website, instagram, facebook, location

Requirements
Must have
• logo and info
Nice to have
• the icons for cell, instagram, email, fb etc
Should not have
• images of people

```html
<!DOCTYPE html>
<html lang="en">
<head>
<meta charset="utf-8">
<title>The Velour Lounge – Business Card</title>
<link href="https://fonts.googleapis.com/css2?family=Poppins:wght@400;500;600&display=swap" rel="stylesheet">
<style>
  :root {
    --backdrop: #1b1b1b;
    --card-black: #0d0d0d;
    --gold: #d6a53c;
    --gold-soft: #c9972f;
    --emboss: #262626;
    --emboss-edge: #303030;
    --rule: #2c2c2c;
  }
  html, body {
    margin: 0;
    padding: 0;
    width: 1200px;
    height: 1200px;
    overflow: hidden;
    background: var(--backdrop);
    font-family: "Poppins", sans-serif;
  }
  .canvas {
    position: relative;
    width: 1200px;
    height: 1200px;
    background: radial-gradient(ellipse at 50% 40%, #262626 0%, var(--backdrop) 70%);
  }
  .card {
    position: absolute;
    left: 170px;
    width: 860px;
    height: 490px;
    background: var(--card-black);
    border-radius: 22px;
    box-shadow: 0 18px 40px rgba(0,0,0,0.55);
    overflow: hidden;
  }
  .card--front { top: 90px; }
  .card--back { top: 620px; }

  /* Front: brand mark */
  .brand-mark {
    position: absolute;
    left: 50%;
    top: 50%;
    transform: translate(-50%, -50%);
    width: 330px;
    height: 330px;
    border: 2px solid var(--gold);
    border-radius: 50%;
    display: flex;
    align-items: center;
    justify-content: center;
  }
  .brand-name {
    color: var(--gold);
    font-weight: 500;
    font-size: 26px;
    letter-spacing: 0.22em;
    text-align: center;
    line-height: 1.5;
    text-transform: uppercase;
  }

  /* Back: details */
  .holder {
    position: absolute;
    left: 60px;
    top: 52px;
    color: var(--gold);
  }
  .holder-name {
    font-weight: 600;
    font-size: 26px;
    letter-spacing: 0.12em;
    text-transform: uppercase;
  }
  .holder-title {
    font-weight: 400;
    font-size: 19px;
    letter-spacing: 0.08em;
    text-transform: uppercase;
    margin-top: 2px;
  }
  .contact {
    position: absolute;
    left: 60px;
    top: 268px;
    color: var(--gold);
    font-size: 19px;
    letter-spacing: 0.06em;
    line-height: 1.45;
  }
  .contact .divider {
    width: 470px;
    height: 1px;
    background: var(--rule);
    margin: 10px 0 12px;
  }
  .footer-rule {
    position: absolute;
    left: 60px;
    right: 60px;
    top: 412px;
    height: 1px;
    background: var(--rule);
  }
  .social {
    position: absolute;
    right: 60px;
    bottom: 28px;
    color: var(--gold);
    font-size: 19px;
    letter-spacing: 0.04em;
  }
  .emboss-mark {
    position: absolute;
    right: 70px;
    top: 110px;
    width: 240px;
    height: 240px;
    border: 2px solid var(--emboss-edge);
    border-radius: 50%;
    display: flex;
    align-items: center;
    justify-content: center;
  }
  .emboss-mark .brand-name {
    color: var(--emboss);
    font-size: 19px;
    text-shadow: 0 1px 0 #1a1a1a;
  }
</style>
</head>
<body>
  <main class="canvas">
    <section class="card card--front" aria-label="Card front">
      <div class="brand-mark">
        <div class="brand-name">The<br>Velour<br>Lounge</div>
      </div>
    </section>

    <section class="card card--back" aria-label="Card back">
      <div class="holder">
        <div class="holder-name">Marcus Ellery</div>
        <div class="holder-title">CEO/Founder</div>
      </div>

      <div class="contact">
        <div>555-204-1187 &nbsp;|&nbsp; hello@velourlounge.com</div>
        <div>www.velourloungestudio.com</div>
        <div class="divider"></div>
        <div>118 Harbor Street West</div>
        <div>Suite 210, Fairhaven, MI 49210</div>
      </div>

      <div class="emboss-mark">
        <div class="brand-name">The<br>Velour<br>Lounge</div>
      </div>

      <div class="footer-rule"></div>
      <div class="social">Find us on : @velourlounge</div>
    </section>
  </main>
</body>
</html>
```